Updated DJ business Card showing other businesses

DJ Kestro offers professional mobile dj services including DJ. MC. Karaoke.
Silent Disco (will attach logo)
I also offer a 360 Photo Booth.

Contact info:
(555) 314-7720
lenny.corbitt@mailvane.net
Social Media @DJKestroBPZ

```html
<!DOCTYPE html>
<html lang="en">
<head>
<meta charset="utf-8">
<title>DJ Kestro Business Card</title>
<link rel="stylesheet" href="https://fonts.googleapis.com/css2?family=Montserrat:wght@400;500;800&display=swap">
<style>
  :root {
    --backdrop: #6e5539;
    --card: #ffffff;
    --ink: #111111;
    --text: #2b2b2b;
    --accent: #d6204a;
  }
  * { margin: 0; padding: 0; box-sizing: border-box; }
  html, body { width: 900px; height: 1200px; overflow: hidden; }
  body {
    position: relative;
    background: var(--backdrop);
    font-family: "Montserrat", Arial, sans-serif;
  }
  .card {
    position: absolute;
    left: 80px;
    width: 742px;
    height: 440px;
    background: var(--card);
    border-radius: 38px;
    box-shadow: 0 6px 14px rgba(0,0,0,0.45);
  }
  .card--front { top: 132px; }
  .card--back { top: 638px; }

  .brand-name {
    position: absolute;
    font-weight: 800;
    color: var(--ink);
    letter-spacing: -0.5px;
    line-height: 1;
    white-space: nowrap;
  }
  .card--front .brand-name { left: 58px; top: 194px; font-size: 46px; }

  .divider {
    position: absolute;
    left: 406px;
    top: 190px;
    width: 2px;
    height: 82px;
    background: var(--accent);
  }
  .contact-list {
    position: absolute;
    left: 433px;
    top: 192px;
    list-style: none;
    font-size: 16.5px;
    font-weight: 500;
    color: var(--text);
  }
  .contact-list li {
    display: flex;
    align-items: center;
    gap: 8px;
    height: 23px;
  }
  .contact-list svg { width: 14px; height: 14px; flex: none; }
  .social-dot {
    width: 14px;
    height: 14px;
    border-radius: 50%;
    background: var(--accent);
    flex: none;
  }

  .card--back .brand-name {
    left: 0;
    width: 100%;
    text-align: center;
    top: 94px;
    font-size: 66px;
  }
  .service-mark {
    position: absolute;
    left: 168px;
    top: 232px;
    display: flex;
    align-items: center;
    gap: 24px;
  }
  .service-mark__circle {
    width: 112px;
    height: 112px;
    border-radius: 50%;
    background: var(--ink);
  }
  .service-mark__name {
    font-weight: 800;
    font-size: 44px;
    line-height: 1.05;
    color: var(--ink);
    letter-spacing: 1px;
  }
</style>
</head>
<body>
  <section class="card card--front">
    <div class="brand-name">DJ KESTRO</div>
    <div class="divider"></div>
    <ul class="contact-list">
      <li>
        <svg viewBox="0 0 14 14" aria-hidden="true"><path fill="#d6204a" d="M1 5c0-2 2.5-3 6-3s6 1 6 3v1.2H10V4.8H4v1.4H1z M3 7h8l1.5 5h-11z M7 8.3a1.5 1.5 0 1 0 0.01 0z"/></svg>
        <span>(555) 314-7720</span>
      </li>
      <li>
        <svg viewBox="0 0 14 14" aria-hidden="true"><rect x="1" y="3" width="12" height="8.5" fill="#d6204a"/><path d="M1.5 3.5 7 8l5.5-4.5" fill="none" stroke="#fff" stroke-width="1.2"/></svg>
        <span>lenny.corbitt@mailvane.net</span>
      </li>
      <li>
        <span class="social-dot"></span>
        <span>@DJKestroBPZ</span>
      </li>
    </ul>
  </section>

  <section class="card card--back">
    <div class="brand-name">DJ KESTRO</div>
    <div class="service-mark">
      <div class="service-mark__circle"></div>
      <div class="service-mark__name">SILENT<br>DISCO</div>
    </div>
  </section>
</body>
</html>
```